bottle label/ product label for smoothies (ultra fresh)

Please create a bottle label for our smoothies for retail distribution.
It's important that the following key features are clearly stated:

Ultra-fresh

Handmade

No preservatives

Not heat-treated

No added sugar

The base of the product label should be transparent, so that the color and content of the smoothie can be seen clearly.

We are a young, dynamic company. Our values are honesty, ultra-freshness, and authenticity — and we are the only ones producing this type of product in our country. We are positioned in the premium segment.

Design style: Modern, clean, and natural — but not playful or childish.

Example product: Kelu Kelu (Mango, Pineapple, Lemon, Passion Fruit, Orange)

Wenn du möchtest, kann ich auch gleich einen konkreten Vorschlag für das Etikettendesign auf Englisch oder einen Entwurfstext für das Label selbst erstellen. Sag einfach Bescheid!

Target Market(s)

trade - convenience

Industry/Entity Type

trade

Font styles to use
Sans Serif

Requirements
Must have
• sales- features: Ultra-fresh Handmade No preservatives Not heat-treated No added sugar

```html
<!DOCTYPE html>
<html lang="en">
<head>
<meta charset="utf-8">
<title>Kelu Kelu – smoothie bottle labels</title>
<link rel="stylesheet" href="https://fonts.googleapis.com/css2?family=League+Spartan:wght@700;900&family=Lexend:wght@500;600&family=Gochi+Hand&display=swap">
<style>
  :root {
    --ink: #111111;
    --cap: #262626;
    --cap-rib: #4a4a4a;
    --paper: #ffffff;
    --lemon: #f2b705;
    --orange: #ff6200;
    --pineapple: #f39519;
    --lemon-fruit: #f9a51b;
    --orange-fruit: #e85a0c;
    --pineapple-fruit: #c98a1e;
    --white: #ffffff;
  }
  * { margin: 0; padding: 0; box-sizing: border-box; }
  html, body { width: 1200px; height: 1000px; overflow: hidden; background: var(--paper); }
  .canvas { position: relative; width: 1200px; height: 1000px; }
  .bottles { position: absolute; inset: 0; }

  .label {
    position: absolute;
    top: 0;
    width: 285px;
    height: 1000px;
    text-align: center;
    color: var(--ink);
  }
  .label--lemon { left: 143px; }
  .label--orange { left: 458px; }
  .label--pineapple { left: 773px; }

  .brand {
    position: absolute; top: 284px; left: 0; right: 0;
    font-family: "Lexend", sans-serif; font-weight: 600; font-size: 27px;
    letter-spacing: 0.3px;
  }
  .product-name {
    position: absolute; top: 432px; left: 0; right: 0;
    font-family: "League Spartan", sans-serif; font-weight: 900;
    font-size: 92px; line-height: 72px; letter-spacing: 1px;
  }
  .flavour {
    position: absolute; top: 580px; left: 0; right: 0;
    display: flex; justify-content: center; align-items: center; gap: 8px;
    font-family: "Gochi Hand", cursive; font-size: 40px; line-height: 44px;
    color: var(--white);
  }
  .fruit-art {
    display: inline-block; width: 34px; height: 34px; border-radius: 50%;
    border: 2px solid var(--ink);
  }
  .fruit-art--lemon { background: var(--lemon-fruit); }
  .fruit-art--orange { background: var(--orange-fruit); }
  .fruit-art--pineapple { background: linear-gradient(180deg, #3aa530 0 35%, var(--pineapple-fruit) 35%); }

  .claim {
    position: absolute; top: 672px; left: 0; right: 0;
    font-family: "Lexend", sans-serif; font-weight: 500; font-size: 41px;
    line-height: 46px; letter-spacing: -0.5px;
  }
  .claim-sub {
    position: absolute; top: 708px; left: 0; right: 0;
    font-family: "Gochi Hand", cursive; font-size: 30px; line-height: 34px;
  }
  .features {
    position: absolute; top: 812px; left: 22px; right: 22px;
    display: flex; justify-content: space-between;
  }
  .feature {
    display: flex; align-items: center; gap: 3px;
    height: 26px; padding: 0 4px;
    background: var(--ink); color: var(--white); border-radius: 2px;
    font-family: "Lexend", sans-serif; font-weight: 600;
    font-size: 7px; line-height: 7.5px; text-align: left; text-transform: uppercase;
  }
  .feature svg { width: 16px; height: 16px; flex: none; }
  .volume {
    position: absolute; top: 857px; left: 0; right: 0;
    font-family: "League Spartan", sans-serif; font-weight: 700; font-size: 15px;
  }
</style>
</head>
<body>
<div class="canvas">

  <svg class="bottles" width="1200" height="1000" viewBox="0 0 1200 1000" aria-hidden="true">
    <defs>
      <pattern id="cap-ribs" width="4" height="10" patternUnits="userSpaceOnUse">
        <rect width="4" height="10" fill="var(--cap)"/>
        <rect x="2.5" width="1" height="10" fill="var(--cap-rib)"/>
      </pattern>
      <g id="bottle-cap">
        <rect x="-90" y="78" width="180" height="52" rx="10" fill="url(#cap-ribs)" stroke="var(--ink)" stroke-width="1"/>
        <rect x="-92" y="128" width="184" height="14" rx="2" fill="var(--cap)" stroke="var(--ink)" stroke-width="1"/>
        <rect x="-92" y="143" width="184" height="12" rx="2" fill="var(--cap)" stroke="var(--ink)" stroke-width="1"/>
        <rect x="-92" y="157" width="184" height="6" rx="3" fill="var(--paper)" stroke="var(--ink)" stroke-width="1"/>
      </g>
    </defs>

    <g class="bottle bottle--lemon" transform="translate(285 0)">
      <path d="M-88,163 L-88,192 L-125,228 Q-142,246 -142,275 L-142,880 Q-142,908 -114,908 L114,908 Q142,908 142,880 L142,275 Q142,246 125,228 L88,192 L88,163 Z" fill="var(--paper)" stroke="var(--ink)" stroke-width="1.2"/>
      <path d="M-88,180 L-88,192 L-125,228 Q-142,246 -142,275 L-142,880 Q-142,908 -114,908 L114,908 Q142,908 142,880 L142,275 Q142,246 125,228 L88,192 L88,180 Z" fill="var(--lemon)" stroke="var(--ink)" stroke-width="1.2"/>
      <use href="#bottle-cap"/>
    </g>
    <g class="bottle bottle--orange" transform="translate(600 0)">
      <path d="M-88,163 L-88,192 L-125,228 Q-142,246 -142,275 L-142,880 Q-142,908 -114,908 L114,908 Q142,908 142,880 L142,275 Q142,246 125,228 L88,192 L88,163 Z" fill="var(--paper)" stroke="var(--ink)" stroke-width="1.2"/>
      <path d="M-88,180 L-88,192 L-125,228 Q-142,246 -142,275 L-142,880 Q-142,908 -114,908 L114,908 Q142,908 142,880 L142,275 Q142,246 125,228 L88,192 L88,180 Z" fill="var(--orange)" stroke="var(--ink)" stroke-width="1.2"/>
      <use href="#bottle-cap"/>
    </g>
    <g class="bottle bottle--pineapple" transform="translate(915 0)">
      <path d="M-88,163 L-88,192 L-125,228 Q-142,246 -142,275 L-142,880 Q-142,908 -114,908 L114,908 Q142,908 142,880 L142,275 Q142,246 125,228 L88,192 L88,163 Z" fill="var(--paper)" stroke="var(--ink)" stroke-width="1.2"/>
      <path d="M-88,180 L-88,192 L-125,228 Q-142,246 -142,275 L-142,880 Q-142,908 -114,908 L114,908 Q142,908 142,880 L142,275 Q142,246 125,228 L88,192 L88,180 Z" fill="var(--pineapple)" stroke="var(--ink)" stroke-width="1.2"/>
      <use href="#bottle-cap"/>
    </g>
  </svg>

  <section class="label label--lemon">
    <p class="brand">verano</p>
    <h2 class="product-name">KELU<br>KELU</h2>
    <p class="flavour"><span class="fruit-art fruit-art--lemon" role="img" aria-label="Illustration of a lemon slice"></span>lemon</p>
    <p class="claim">ultra-fresh</p>
    <p class="claim-sub">handmade</p>
    <ul class="features">
      <li class="feature"><svg viewBox="0 0 16 16"><path d="M8 2 L14 5 L14 11 L8 14 L2 11 L2 5 Z M2 5 L8 8 L14 5 M8 8 L8 14" fill="none" stroke="#fff" stroke-width="1.2"/></svg>No sugar<br>added</li>
      <li class="feature"><svg viewBox="0 0 16 16"><path d="M6 2 H10 M7 2 V7 L3 14 H13 L9 7 V2" fill="none" stroke="#fff" stroke-width="1.2"/></svg>No added<br>preservatives</li>
      <li class="feature"><svg viewBox="0 0 16 16"><path d="M8 2 C10 6 13 8 12 11 C11 14 5 14 4 11 C3 8 6 7 8 2 Z" fill="none" stroke="#fff" stroke-width="1.2"/></svg>Not heat-<br>treated</li>
    </ul>
    <p class="volume">250mL</p>
  </section>

  <section class="label label--orange">
    <p class="brand">verano</p>
    <h2 class="product-name">KELU<br>KELU</h2>
    <p class="flavour"><span class="fruit-art fruit-art--orange" role="img" aria-label="Illustration of an orange"></span>orange</p>
    <p class="claim">ultra-fresh</p>
    <p class="claim-sub">handmade</p>
    <ul class="features">
      <li class="feature"><svg viewBox="0 0 16 16"><path d="M8 2 L14 5 L14 11 L8 14 L2 11 L2 5 Z M2 5 L8 8 L14 5 M8 8 L8 14" fill="none" stroke="#fff" stroke-width="1.2"/></svg>No sugar<br>added</li>
      <li class="feature"><svg viewBox="0 0 16 16"><path d="M6 2 H10 M7 2 V7 L3 14 H13 L9 7 V2" fill="none" stroke="#fff" stroke-width="1.2"/></svg>No added<br>preservatives</li>
      <li class="feature"><svg viewBox="0 0 16 16"><path d="M8 2 C10 6 13 8 12 11 C11 14 5 14 4 11 C3 8 6 7 8 2 Z" fill="none" stroke="#fff" stroke-width="1.2"/></svg>Not heat-<br>treated</li>
    </ul>
    <p class="volume">250mL</p>
  </section>

  <section class="label label--pineapple">
    <p class="brand">verano</p>
    <h2 class="product-name">KELU<br>KELU</h2>
    <p class="flavour"><span class="fruit-art fruit-art--pineapple" role="img" aria-label="Illustration of a pineapple"></span>pineapple</p>
    <p class="claim">ultra-fresh</p>
    <p class="claim-sub">handmade</p>
    <ul class="features">
      <li class="feature"><svg viewBox="0 0 16 16"><path d="M8 2 L14 5 L14 11 L8 14 L2 11 L2 5 Z M2 5 L8 8 L14 5 M8 8 L8 14" fill="none" stroke="#fff" stroke-width="1.2"/></svg>No sugar<br>added</li>
      <li class="feature"><svg viewBox="0 0 16 16"><path d="M6 2 H10 M7 2 V7 L3 14 H13 L9 7 V2" fill="none" stroke="#fff" stroke-width="1.2"/></svg>No added<br>preservatives</li>
      <li class="feature"><svg viewBox="0 0 16 16"><path d="M8 2 C10 6 13 8 12 11 C11 14 5 14 4 11 C3 8 6 7 8 2 Z" fill="none" stroke="#fff" stroke-width="1.2"/></svg>Not heat-<br>treated</li>
    </ul>
    <p class="volume">250mL</p>
  </section>

</div>
</body>
</html>
```